Consultancy Business Card Design

We need a business card design for a new company based in singapore called FortyOne. FortyOne a boutique consultancy firm offering broad-based business solutions, from conception to re-invention, for ventures from new start-ups to long-running traditional businesses.
Its 2 main divisions (Food & Beverage Operations and Construction & Project Management) have access to a wide range of networks, knowledge bases, and resources to service its clients across numerous diverse sectors. This includes, and is not limited to, construction, F&B, and retail.
We are a company that combines the ambition, boldness and energy of one in the 20s with the dedication, level-headedness and dependability of one entering its 30s. Bridging the experiences of the old with ideals of the young, we draw on the positives of both to create a unique synergy.
We hope to see designs that fits our company profile.
Boutique
Contact Information for Business Card
FortyOne(Company Name)
Marcus Tan (Name)
Principle Consultant (Title)
F&B and Hospitality (Division)
(+65) 8364 5107 (Contact no.)
marcus@fortyone-example.com.sg (Email)
Colors
Designer to choose colors to be used in the design.

```html
<!DOCTYPE html>
<html lang="en">
<head>
<meta charset="utf-8">
<title>FortyOne Business Card</title>
<link rel="stylesheet" href="https://fonts.googleapis.com/css2?family=Open+Sans:wght@400;600;700&display=swap">
<style>
  :root {
    --canvas: #e6e7ea;
    --card: #ffffff;
    --brand-blue: #18b6e8;
    --stripe-blue: #1a9fd4;
    --stripe-deep: #0d5f86;
    --band-dark: #4a4b4f;
    --band-darker: #3a3b3e;
    --panel-light: #d3d4d7;
    --ink: #3b3c40;
    --white: #ffffff;
  }
  * { box-sizing: border-box; margin: 0; padding: 0; }
  html, body {
    width: 1200px;
    height: 900px;
    overflow: hidden;
    background: var(--canvas);
    font-family: "Open Sans", Arial, sans-serif;
  }
  .card {
    position: absolute;
    width: 680px;
    height: 388px;
    background: var(--card);
    box-shadow: 0 6px 18px rgba(0,0,0,0.18);
    overflow: hidden;
  }
  .card--front { left: 260px; top: 40px; }
  .card--back  { left: 260px; top: 472px; }

  .wordmark {
    position: absolute;
    color: var(--brand-blue);
    font-weight: 700;
    letter-spacing: 0.5px;
    line-height: 1;
  }
  .card--front .wordmark {
    left: 0; right: 0; top: 150px;
    text-align: center;
    font-size: 84px;
  }
  .card--back .wordmark {
    left: 150px; top: 86px;
    font-size: 52px;
  }

  .card__graphics { position: absolute; inset: 0; }

  .identity {
    position: absolute;
    left: 32px;
    top: 252px;
    color: var(--white);
    font-variant: small-caps;
    line-height: 1.05;
  }
  .identity__name { font-size: 27px; font-weight: 600; }
  .identity__role { font-size: 17px; font-weight: 400; margin-top: 3px; }

  .contact {
    position: absolute;
    display: flex;
    align-items: center;
    gap: 10px;
    color: var(--ink);
    font-size: 17px;
    letter-spacing: 0.3px;
  }
  .contact svg { width: 20px; height: 20px; flex: none; }
  .contact--phone { left: 478px; top: 272px; }
  .contact--email { left: 418px; top: 340px; }
</style>
</head>
<body>

<section class="card card--front" aria-label="Card front">
  <div class="wordmark">FortyOne</div>
</section>

<section class="card card--back" aria-label="Card back">
  <svg class="card__graphics" viewBox="0 0 680 388" aria-hidden="true">
    <defs>
      <linearGradient id="bandShade" x1="0" y1="0" x2="0" y2="1">
        <stop offset="0" stop-color="#55565a"/>
        <stop offset="1" stop-color="#3a3b3e"/>
      </linearGradient>
      <linearGradient id="panelShade" x1="0" y1="0" x2="1" y2="1">
        <stop offset="0" stop-color="#dcdde0"/>
        <stop offset="1" stop-color="#c4c5c9"/>
      </linearGradient>
      <linearGradient id="stripeShade" x1="0" y1="0" x2="1" y2="0">
        <stop offset="0" stop-color="#1a9fd4"/>
        <stop offset="0.6" stop-color="#0d5f86"/>
        <stop offset="1" stop-color="#9fd3ea"/>
      </linearGradient>
    </defs>
    <!-- upper accent strip -->
    <polygon points="400,226 680,220 680,240 386,246" fill="var(--band-darker)"/>
    <!-- main dark band -->
    <polygon points="0,246 680,240 680,388 0,388" fill="url(#bandShade)"/>
    <!-- light contact panel -->
    <polygon points="452,256 680,252 680,388 336,388" fill="url(#panelShade)" stroke="var(--white)" stroke-width="4"/>
    <!-- blue stripe -->
    <rect x="0" y="322" width="420" height="13" fill="var(--stripe-blue)"/>
    <polygon points="414,322 680,300 680,311 414,335" fill="url(#stripeShade)"/>
  </svg>

  <div class="wordmark">FortyOne</div>

  <div class="identity">
    <p class="identity__name">Marcus Tan</p>
    <p class="identity__role">Principle Consultant</p>
    <p class="identity__role">F&amp;B and Hospitality</p>
  </div>

  <p class="contact contact--phone">
    <svg viewBox="0 0 24 24" aria-hidden="true"><path fill="#3b3c40" d="M6.6 10.8a15 15 0 0 0 6.6 6.6l2.2-2.2c.3-.3.7-.4 1-.2 1.1.4 2.3.6 3.6.6.6 0 1 .4 1 1V20c0 .6-.4 1-1 1A17 17 0 0 1 3 4c0-.6.4-1 1-1h3.5c.6 0 1 .4 1 1 0 1.3.2 2.5.6 3.6.1.3 0 .7-.2 1z"/></svg>
    (+65) 8364 5107
  </p>
  <p class="contact contact--email">
    <svg viewBox="0 0 24 24" aria-hidden="true"><rect x="2" y="5" width="20" height="14" fill="none" stroke="#3b3c40" stroke-width="2"/><path d="M2 5l10 8 10-8" fill="none" stroke="#3b3c40" stroke-width="2"/></svg>
    marcus@fortyone-example.com.sg
  </p>
</section>

</body>
</html>
```